Postcard Design/Coupon

My business is a Pizza Shop/Restaurant/Bar. I know confusing. I sell mainly pizza and beer but sandwich's and salads are a big seller also. So I want coupons/postcards that I can hand out to every table that comes in to entice them to come back. I also will be sending these coupons/postcards to delivery customers. The business name is Larkdale Pizza Vento address is 581 Thistle Avenue Sewickley PA15143 phone number is 412-741-1744On one side I wanted the coupon offer and logo and the other side the hours but also room for me to send some out.

Target Market(s)

Families

Industry/Entity Type

Restaurant

Requirements
Must have
• Pizza
Nice to have
• Salads/Hoagies/Nice Description

```html
<!DOCTYPE html>
<html lang="en">
<head>
<meta charset="utf-8">
<title>Larkdale Pizza Vento – Postcard Coupon</title>
<link rel="stylesheet" href="https://fonts.googleapis.com/css2?family=Patrick+Hand&family=Amatic+SC:wght@700&family=Fira+Sans+Condensed:wght@500&display=swap">
<style>
  :root {
    --red-dark: #7a0d0d;
    --red: #a3151a;
    --red-bright: #c8202a;
    --white: #ffffff;
    --page: #d9d6d2;
    --wood-light: #e7e3de;
    --hours-green: #4f9a3a;
    --hours-red: #9c141a;
    --salad-green: #5f9a34;
    --salad-leaf: #8cc04a;
    --tomato: #c7352a;
    --bread: #d9b07a;
    --bread-light: #efe1c8;
    --beer: #e0a22e;
    --barrel: #7a4a26;
    --crust: #d89a4a;
    --cheese: #f0c766;
    --sauce: #c43a26;
  }
  * { box-sizing: border-box; margin: 0; padding: 0; }
  html, body { width: 1200px; height: 1000px; overflow: hidden; }
  body { background: var(--page); position: relative; font-family: "Patrick Hand", cursive; }

  .postcard {
    position: absolute; width: 680px; height: 460px; overflow: hidden;
    background: var(--white); box-shadow: 0 6px 18px rgba(0,0,0,.25);
  }
  .postcard--front { left: 40px; top: 30px; }
  .postcard--back { left: 480px; top: 510px; }

  .banner {
    position: absolute; left: 0; top: 0; width: 100%; z-index: 3;
    background: linear-gradient(to bottom, var(--red) 0%, var(--red-dark) 100%);
    color: var(--white);
  }
  .postcard--front .banner { height: 92px; }
  .postcard--back .banner { height: 112px; }
  .ribbon { position: absolute; left: 18px; top: 0; z-index: 4; }
  .brand-name {
    position: absolute; white-space: nowrap;
    font-family: "Patrick Hand", cursive; letter-spacing: 1px;
    text-transform: uppercase; color: var(--white);
  }
  .postcard--front .brand-name { left: 62px; top: 46px; font-size: 30px; }
  .postcard--back .brand-name { left: 130px; top: 56px; font-size: 38px; }
  .contact {
    position: absolute; right: 20px; top: 14px; text-align: right;
    font-family: "Fira Sans Condensed", sans-serif; font-size: 16px; line-height: 1.75;
  }

  .photo { position: absolute; }
  .photo--salad {
    left: 0; top: 92px; width: 232px; height: 368px;
    background:
      radial-gradient(circle at 70% 35%, var(--tomato) 0%, rgba(199,53,42,0) 28%),
      radial-gradient(circle at 30% 60%, var(--salad-leaf) 0%, rgba(140,192,74,0) 45%),
      linear-gradient(170deg, #7fb04a 0%, var(--salad-green) 55%, #e9ecd9 100%);
  }
  .photo--sandwich {
    left: 236px; top: 92px; width: 220px; height: 368px;
    background:
      radial-gradient(ellipse at 60% 40%, var(--bread-light) 0%, rgba(239,225,200,0) 45%),
      radial-gradient(circle at 55% 55%, #cf5a3a 0%, rgba(207,90,58,0) 20%),
      linear-gradient(170deg, var(--bread-light) 0%, var(--bread) 55%, #a8703f 100%);
  }
  .photo--beer {
    left: 460px; top: 92px; width: 220px; height: 368px;
    background:
      radial-gradient(ellipse at 72% 40%, var(--beer) 0%, rgba(224,162,46,0) 32%),
      linear-gradient(100deg, var(--barrel) 0%, #a46a3a 45%, #e7d8c4 100%);
  }
  .photo-divider { position: absolute; top: 92px; width: 4px; height: 368px; background: var(--white); z-index: 1; }

  .tag {
    position: absolute; width: 38px; z-index: 2;
    background: var(--red-bright); color: var(--white); border-radius: 0 0 3px 3px;
    display: flex; align-items: center; justify-content: center;
    box-shadow: 0 2px 4px rgba(0,0,0,.3);
  }
  .tag span { transform: rotate(-90deg); font-size: 21px; letter-spacing: 1px; white-space: nowrap; }
  .tag--salad { left: 96px; top: 120px; height: 96px; }
  .tag--sandwich { left: 294px; top: 110px; height: 120px; }
  .tag--beer { left: 502px; top: 96px; height: 80px; }

  .pizza-plate {
    position: absolute; left: 180px; top: 300px; width: 420px; height: 420px; border-radius: 50%;
    border: 8px solid var(--white); z-index: 2;
    background:
      radial-gradient(circle at 35% 30%, var(--sauce) 0%, rgba(196,58,38,0) 22%),
      radial-gradient(circle at 62% 28%, #4f7a2a 0%, rgba(79,122,42,0) 22%),
      radial-gradient(circle, var(--cheese) 0%, #e8a04a 62%, var(--crust) 78%, #b87434 100%);
  }
  .coupon-seal { position: absolute; left: 470px; top: 262px; z-index: 3; }

  .photo--pizza-back {
    left: 0; top: 0; width: 680px; height: 400px;
    background:
      radial-gradient(circle at 45% 70%, var(--cheese) 0%, rgba(240,199,102,0) 30%),
      radial-gradient(circle at 12% 80%, #3f8a2a 0%, rgba(63,138,42,0) 35%),
      linear-gradient(100deg, #4a8a2a 0%, var(--tomato) 28%, var(--crust) 55%, #ead9b8 100%);
  }
  .mail-area { position: absolute; left: 360px; top: 112px; width: 320px; height: 276px; background: rgba(255,255,255,.8); z-index: 1; }
  .hours {
    position: absolute; left: 92px; top: 162px; width: 200px; height: 222px; z-index: 2;
    background: rgba(255,255,255,.9); border-radius: 14px; padding: 14px 10px 0 22px;
    font-family: "Amatic SC", cursive; color: var(--hours-red);
  }
  .hours__title { color: var(--hours-green); font-size: 27px; line-height: 1.1; margin-bottom: 4px; font-weight: 700; }
  .hours__list { list-style: none; font-size: 21px; line-height: 1.22; }
  .call-strip {
    position: absolute; left: 0; top: 392px; width: 680px; height: 68px; z-index: 2;
    background: var(--wood-light); border-top: 5px solid var(--red);
    font-family: "Amatic SC", cursive; color: var(--red);
    font-size: 40px; letter-spacing: 3px; padding-left: 120px; line-height: 62px; white-space: nowrap;
  }
</style>
</head>
<body>

<section class="postcard postcard--front" aria-label="Coupon side">
  <header class="banner">
    <p class="brand-name">Larkdale Pizza Vento</p>
    <p class="contact">581 Thistle Avenue Sewickley PA15143<br>CALL US 412-555-0187</p>
  </header>
  <svg class="ribbon" width="34" height="106" viewBox="0 0 34 106" aria-hidden="true">
    <path d="M0 0 H34 V106 L17 92 L0 106 Z" fill="#b01a1f"/>
    <path d="M0 0 H6 V106 H0 Z" fill="#6b0a0a"/>
  </svg>

  <div class="photo photo--salad" role="img" aria-label="Photo of a fresh garden salad with cucumber, tomato, olives and feta"></div>
  <div class="photo photo--sandwich" role="img" aria-label="Photo of a sliced hoagie sandwich with tomato and lettuce"></div>
  <div class="photo photo--beer" role="img" aria-label="Photo of a glass of beer beside a wooden barrel"></div>
  <div class="photo-divider" style="left:232px"></div>
  <div class="photo-divider" style="left:456px"></div>

  <div class="tag tag--salad"><span>SALAD</span></div>
  <div class="tag tag--sandwich"><span>SANDWICH</span></div>
  <div class="tag tag--beer"><span>BEER</span></div>

  <div class="pizza-plate" role="img" aria-label="Photo of pizza slices with pepperoni, mushroom and pesto toppings"></div>

  <svg class="coupon-seal" width="170" height="170" viewBox="0 0 170 170" aria-label="Pizza 5% discount with this coupon">
    <polygon fill="#5a0b0b" points="85,4 93,14 104,6 109,18 121,13 123,26 136,24 135,37 148,38 144,51 156,55 149,66 160,73 150,82 159,91 148,98 155,109 142,113 146,126 133,127 134,140 121,138 118,151 106,146 100,158 90,149 81,160 73,149 62,157 57,145 44,149 42,136 29,137 30,124 17,121 22,109 10,103 19,94 9,85 19,77 10,67 22,61 17,49 30,46 29,33 42,33 45,20 57,24 62,12 73,18 78,6"/>
    <circle cx="85" cy="83" r="66" fill="none" stroke="#ffffff" stroke-width="1.5" stroke-dasharray="3 3"/>
    <text x="85" y="72" text-anchor="middle" fill="#ffffff" font-family="Patrick Hand, cursive" font-size="36">PIZZA</text>
    <text x="58" y="104" text-anchor="middle" fill="#ffffff" font-family="Patrick Hand, cursive" font-size="32">5%</text>
    <text x="106" y="100" text-anchor="middle" fill="#ffffff" font-family="Patrick Hand, cursive" font-size="13">DISCOUNT</text>
    <text x="100" y="116" text-anchor="middle" fill="#ffffff" font-family="Patrick Hand, cursive" font-size="13">WITH THIS</text>
    <text x="92" y="131" text-anchor="middle" fill="#ffffff" font-family="Patrick Hand, cursive" font-size="13">COUPON</text>
  </svg>
</section>

<section class="postcard postcard--back" aria-label="Hours and mailing side">
  <div class="photo photo--pizza-back" role="img" aria-label="Photo of a vegetable pizza with peppers, tomatoes and green onions"></div>
  <header class="banner">
    <p class="brand-name">Larkdale Pizza Vento</p>
  </header>
  <svg class="ribbon" width="40" height="126" viewBox="0 0 40 126" style="left:80px" aria-hidden="true">
    <path d="M0 0 H40 V126 L20 110 L0 126 Z" fill="#b01a1f"/>
    <path d="M0 0 H7 V126 H0 Z" fill="#6b0a0a"/>
  </svg>

  <div class="mail-area" aria-label="Mailing address area"></div>

  <div class="hours">
    <h2 class="hours__title">OPENING HOURS</h2>
    <ul class="hours__list">
      <li>MON 8 AM – 20 PM</li>
      <li>TUE 8 AM – 20 PM</li>
      <li>WED 8 AM – 20 PM</li>
      <li>THU 8 AM – 20 PM</li>
      <li>FRI 8 AM – 20 PM</li>
      <li>SAT 9 AM – 21 PM</li>
    </ul>
  </div>

  <p class="call-strip">CALL TO ORDER 412-555-0187</p>
</section>

</body>
</html>
```